I would like to purchase a customized version of a design you have previously submitted - https://www.artquarry.net/design/5291847<br/><br/>I need a design for a swimming pool business card. The services we provide are Maintenance, Repairs and Installations so if you include that in the card. I would also like my email bluecrestpoolsservice@maildrift.net, my address 48317 Corvella Dr. Ashmont CA, phone number 530-617-2384. Id like to have the two o's in Bluecrest Pools look like an actual pool.

```html
<!DOCTYPE html>
<html lang="en">
<head>
<meta charset="utf-8">
<title>Bluecrest Pools Services – Business Card</title>
<link rel="stylesheet" href="https://fonts.googleapis.com/css2?family=Open+Sans:ital,wght@0,300;0,400;0,600;0,700;1,700&display=swap">
<style>
  :root {
    --page-bg: #d9dadc;
    --card-bg: #000000;
    --brand-blue: #1e6fd0;
    --text-light: #d4d6d8;
    --rule: #5a5c60;
  }
  * { box-sizing: border-box; margin: 0; padding: 0; }
  html, body { width: 1200px; height: 1200px; overflow: hidden; }
  body {
    background: var(--page-bg);
    font-family: "Open Sans", Arial, sans-serif;
    display: flex;
    flex-direction: column;
    align-items: center;
    justify-content: center;
    gap: 44px;
  }
  .card {
    width: 900px;
    height: 514px;
    background: var(--card-bg);
    position: relative;
    color: var(--text-light);
  }
  .brand-dot {
    border-radius: 50%;
    background: var(--brand-blue);
    flex: none;
  }

  /* Front */
  .card-front {
    display: flex;
    align-items: center;
    justify-content: center;
    gap: 40px;
  }
  .card-front .brand-dot { width: 150px; height: 150px; }
  .card-front .divider { width: 2px; height: 180px; background: var(--rule); }
  .front-wordmark {
    font-size: 50px;
    font-weight: 600;
    line-height: 1;
    letter-spacing: 1px;
    text-transform: uppercase;
  }
  .front-tagline {
    margin-top: 22px;
    font-size: 27px;
    color: var(--brand-blue);
  }

  /* Back */
  .card-back { padding: 66px 64px; }
  .back-header { display: flex; align-items: center; gap: 26px; }
  .card-back .brand-dot { width: 104px; height: 104px; }
  .back-wordmark {
    font-size: 44px;
    font-weight: 600;
    line-height: 1;
    text-transform: uppercase;
    letter-spacing: 0.5px;
  }
  .back-tagline { margin-top: 8px; font-size: 21px; color: var(--brand-blue); }
  .back-body { display: flex; margin-top: 56px; }
  .holder-name {
    width: 300px;
    font-size: 36px;
    font-weight: 700;
    font-style: italic;
    color: var(--brand-blue);
  }
  .back-body .divider { width: 2px; height: 190px; background: var(--rule); margin-right: 30px; }
  .contact-list { list-style: none; display: flex; flex-direction: column; gap: 16px; }
  .contact-item { display: flex; align-items: flex-start; gap: 16px; font-size: 24px; line-height: 1.25; }
  .contact-item svg { width: 26px; height: 26px; flex: none; margin-top: 3px; }
</style>
</head>
<body>

<section class="card card-front">
  <span class="brand-dot"></span>
  <span class="divider"></span>
  <div class="front-text">
    <p class="front-wordmark">Bluecrest Pools<br>Services</p>
    <p class="front-tagline">Maintenance, Repairs &amp; Installations</p>
  </div>
</section>

<section class="card card-back">
  <header class="back-header">
    <span class="brand-dot"></span>
    <div>
      <p class="back-wordmark">Bluecrest Pools Services</p>
      <p class="back-tagline">Maintenance, Repairs &amp; Installations</p>
    </div>
  </header>
  <div class="back-body">
    <p class="holder-name">Marco Delgado</p>
    <span class="divider"></span>
    <ul class="contact-list">
      <li class="contact-item">
        <svg viewBox="0 0 24 24" fill="none" stroke="#1e6fd0" stroke-width="2"><rect x="6" y="2" width="12" height="20" rx="2"/><line x1="10" y1="18" x2="14" y2="18"/></svg>
        <span>530-617-2384</span>
      </li>
      <li class="contact-item">
        <svg viewBox="0 0 24 24" fill="none" stroke="#1e6fd0" stroke-width="2"><rect x="2" y="5" width="20" height="14" rx="1"/><polyline points="2,6 12,13 22,6"/></svg>
        <span>bluecrestpoolsservice@maildrift.net</span>
      </li>
      <li class="contact-item">
        <svg viewBox="0 0 24 24" fill="#1e6fd0"><path d="M12 3 2 12h3v9h5v-6h4v6h5v-9h3z"/></svg>
        <span>48317 Corvella Dr. Ashmont,<br>95412 CA</span>
      </li>
    </ul>
  </div>
</section>

</body>
</html>
```